selling natural honey, a sticker showing scenery and creating interest for consumers

i need a design that portrays a natural product and has an energetic feel about it. the product is natural honey from the country. The honey is sourced from the South Burnett region of Queensland and will be sold to stores. The company selling the product is Marrowick Provisions. The sticker needs to be energetic and also interesting with a level of sophistication.

25-50 mainly females who enjoy natural prducts and willing to pay for good qaulity

It Company

• a nice scenery background, like hills or open paddocks to portray a country/ natural product.

must have 'Marrowick Provisions'

and

'Tarrowin Vale Honey'

included on the sticker
• scenery, maybe a bee or two flying around.
• can't have too much of a cartoon look.

needs to be relatively simple and elegant

```html
<!DOCTYPE html>
<html lang="en">
<head>
<meta charset="utf-8">
<title>Tarrowin Vale Honey – Jar Sticker</title>
<link href="https://fonts.googleapis.com/css2?family=Crimson+Text:wght@700&family=Barlow+Condensed:wght@600&display=swap" rel="stylesheet">
<style>
  :root {
    --canvas: #ffffff;
    --frame-orange: #f7a935;
    --frame-line: #ffffff;
    --badge-orange: #f6a334;
    --badge-edge: #fdf3df;
    --sky-glow: #fbe58a;
    --sun-haze: #e9c75a;
    --canopy: #8c8640;
    --canopy-deep: #5c5f2c;
    --meadow: #86a843;
    --meadow-deep: #5f8a2e;
    --ink: #141414;
  }
  * { margin: 0; padding: 0; box-sizing: border-box; }
  html, body {
    width: 1200px;
    height: 1000px;
    overflow: hidden;
    background: var(--canvas);
  }
  .canvas {
    position: relative;
    width: 1200px;
    height: 1000px;
  }
  .sticker {
    position: absolute;
    left: 300px;
    top: 200px;
    width: 600px;
    height: 600px;
  }
  .sticker-frame {
    position: absolute;
    inset: 0;
    width: 600px;
    height: 600px;
  }
  .scenery {
    position: absolute;
    left: 16px;
    top: 16px;
    width: 568px;
    height: 568px;
    background:
      radial-gradient(ellipse 70% 45% at 42% 8%, var(--sky-glow) 0%, rgba(251,229,138,0) 70%),
      linear-gradient(180deg,
        var(--sun-haze) 0%,
        var(--canopy) 40%,
        var(--canopy-deep) 64%,
        var(--meadow) 76%,
        var(--meadow-deep) 100%);
  }
  .badge {
    position: absolute;
    left: 162px;
    top: 90px;
    width: 288px;
    height: 324px;
  }
  .brand-lockup {
    position: absolute;
    left: 0;
    right: 0;
    top: 206px;
    text-align: center;
    font-family: "Crimson Text", Georgia, serif;
    font-weight: 700;
    color: var(--ink);
  }
  .brand-place {
    display: block;
    font-size: 27px;
    line-height: 1;
    margin-left: 60px;
  }
  .brand-product {
    display: block;
    font-size: 116px;
    line-height: 1;
    margin-top: -4px;
  }
  .maker {
    position: absolute;
    left: 0;
    right: 0;
    top: 500px;
    display: flex;
    align-items: center;
    justify-content: center;
    gap: 12px;
    font-family: "Barlow Condensed", "Arial Narrow", sans-serif;
    font-weight: 600;
    font-size: 18px;
    letter-spacing: 0.06em;
    text-transform: uppercase;
    color: var(--ink);
  }
  .maker-rule {
    width: 66px;
    border-top: 2px dashed var(--ink);
  }
</style>
</head>
<body>
<main class="canvas">
  <section class="sticker">
    <svg class="sticker-frame" viewBox="0 0 600 600" aria-hidden="true">
      <path fill="var(--frame-orange)"
            d="M18,0 H582 A18,18 0 0 0 600,18 V582 A18,18 0 0 0 582,600 H18 A18,18 0 0 0 0,582 V18 A18,18 0 0 0 18,0 Z"/>
      <path fill="none" stroke="var(--frame-line)" stroke-width="3"
            d="M24,8 H576 A16,16 0 0 0 592,24 V576 A16,16 0 0 0 576,592 H24 A16,16 0 0 0 8,576 V24 A16,16 0 0 0 24,8 Z"/>
    </svg>
    <div class="scenery" role="img" aria-label="Sunlit open paddock with tall gum trees in golden morning haze over green grass"></div>
    <svg class="badge" viewBox="0 0 288 324" aria-hidden="true">
      <polygon fill="var(--badge-orange)" stroke="var(--badge-edge)" stroke-width="3"
               points="144,3 285,83 285,241 144,321 3,241 3,83"/>
    </svg>
    <h1 class="brand-lockup">
      <span class="brand-place">Tarrowin Vale</span>
      <span class="brand-product">Honey</span>
    </h1>
    <p class="maker"><span class="maker-rule"></span>Marrowick Provisions<span class="maker-rule"></span></p>
  </section>
</main>
</body>
</html>
```